Web site for small printshop

I am looking for a website for small printshop in Iceland, mainly serving university students and artist.

We print posters, flyers, business cards and more.

In addition to our current website, I would like to include design tool, (fx. www.quarvelink.com, www.tandorizo.com or something similar) jobs upload, shopping chart.
Updates

Great work, I am really amazed of the quality of work i am seeing here.

Really way beyond my expectation

GOOD JOB - all of you ! 

Hi all.

The designs submitted have been great, way better than expected.
I really did not expect this level of quality.

Some have been asking me for feedback on their designs, and I will try 
to send some feedback here, without spoiling your creativity.

Likes:
- when the colors of my logo is used in menus, buttons etc.
- simple, not to crowded look.

Dislikes.
- Dark and heavy design
- Lot of text and buttons (crowded look)

Extra info.
- top line (before menus) will contain: Tel - email - language
- menu line will have 5 categories: Home - service - submission of works - FAQ - about us
- 3 large buttons:  Job submit - Job design - ask for offer

LOVE YOUR WORK - great designs so far :)

Target Market(s)

University Students, Artists. Age group 20-30

Industry/Entity Type

University

Requirements
Must have
• The website must be easy to use, clean looking.

```html
<!DOCTYPE html>
<html lang="is">
<head>
<meta charset="utf-8">
<title>Glóprent</title>
<link rel="stylesheet" href="https://fonts.googleapis.com/css2?family=Open+Sans:wght@400;600;700&family=Arimo:wght@400&display=swap">
<style>
:root{
  --sky-deep:#0a4fa8;
  --sky:#1677d4;
  --sky-light:#3b9cec;
  --steel-light:#f4f6f8;
  --steel:#d5dbe1;
  --steel-dark:#9aa4ae;
  --rail:#b9dcf6;
  --paper:#ffffff;
  --ink:#222222;
  --ink-soft:#444444;
  --nav-ink:#6b7278;
  --green:#0c8a3e;
  --green-dark:#06642b;
  --yellow:#f6c400;
  --red:#e2332b;
  --note-red:#e0141e;
  --note-ink:#ffffff;
}
*{box-sizing:border-box;margin:0;padding:0}
html,body{width:1200px;height:900px;overflow:hidden}
body{
  position:relative;
  font-family:"Open Sans",sans-serif;
  background:
    radial-gradient(ellipse 420px 900px at 600px 450px,rgba(120,200,255,.35),transparent 70%),
    linear-gradient(180deg,var(--sky) 0%,var(--sky-deep) 100%);
}
.printer-body{
  position:absolute;left:205px;top:-20px;width:785px;height:160px;
  border-radius:0 0 60px 60px;
  background:linear-gradient(180deg,var(--steel-light) 0%,#e6eaee 60%,var(--steel) 100%);
  box-shadow:0 10px 20px rgba(0,0,0,.35);
}
.printer-window{
  position:absolute;left:380px;top:-10px;width:420px;height:80px;
  border-radius:0 0 50px 50px;
  background:linear-gradient(180deg,#cfd6dc,#eef2f5);
  box-shadow:inset 0 -6px 10px rgba(0,0,0,.12);
}
.printer-window::after{
  content:"";position:absolute;left:25px;top:0;right:25px;height:56px;
  border-radius:0 0 38px 38px;
  background:linear-gradient(180deg,#b8c2ca,#dfe5ea);
}
.rail{
  position:absolute;top:118px;width:40px;height:160px;border-radius:0 0 14px 14px;
  background:linear-gradient(90deg,var(--steel),var(--rail),var(--steel));
}
.rail--left{left:262px}.rail--right{left:900px}
.brand{
  position:absolute;left:252px;top:22px;display:flex;align-items:center;gap:5px;
  font-weight:700;font-size:13px;color:var(--green);
}
.brand__mark{width:12px;height:12px;background:var(--red)}
.tool-button{
  position:absolute;top:5px;width:32px;height:32px;border-radius:50%;
  background:radial-gradient(circle at 40% 35%,#fff,#cfd5da);
  box-shadow:0 1px 3px rgba(0,0,0,.3);
}
.tool-button::after{content:"";position:absolute;left:13px;top:38px;width:6px;height:6px;border-radius:50%;background:#3ab54a}
.tool-button--cart{left:858px}.tool-button--design{left:925px}
.tool-label{position:absolute;left:912px;top:63px;font-size:8px;color:var(--nav-ink)}
.slider{position:absolute;left:856px;top:63px;width:38px;height:7px;border-radius:4px;background:linear-gradient(90deg,#f3d55c 40%,#c7ced4 40%)}
.main-nav{position:absolute;left:338px;top:86px;display:flex;align-items:center;height:22px}
.main-nav a{
  font-size:11px;font-weight:600;color:var(--nav-ink);text-decoration:none;
  padding:0 22px;border-left:1px solid #c5ccd2;line-height:22px;
}
.main-nav a.is-active{
  background:var(--green);color:#fff;border:0;padding:0 18px 0 24px;
  clip-path:polygon(10px 0,100% 0,100% 100%,10px 100%,0 50%);
}
.sheet{
  position:absolute;left:290px;top:120px;width:622px;height:713px;background:var(--paper);
  box-shadow:0 4px 16px rgba(0,0,0,.3);
}
.hero{
  position:absolute;left:13px;top:28px;width:596px;height:217px;border:1px solid #dde2e6;
  background:linear-gradient(100deg,#3a8fd6 0%,#f0bfdc 30%,#f5f6f8 55%,#eef0f3 100%);
}
.hero__title{
  position:absolute;right:22px;bottom:28px;font-size:40px;font-weight:700;color:var(--ink);letter-spacing:.5px;
}
.section-ribbon{
  position:absolute;left:-12px;top:265px;width:294px;height:48px;
  background:linear-gradient(180deg,#14a24b,var(--green-dark));
  clip-path:polygon(0 0,268px 0,100% 50%,268px 100%,0 100%);
  color:#fff;font-weight:700;font-size:16px;line-height:48px;padding-left:112px;
}
.section-title{position:absolute;left:370px;top:278px;font-size:17px;font-weight:700;color:#3b3b3b}
.services{position:absolute;left:20px;top:332px;width:310px}
.service{display:flex;gap:20px;margin-bottom:12px}
.service__icon{width:60px;flex:none;padding-top:12px}
.service h3{font-family:"Arimo",sans-serif;font-weight:400;font-size:11.5px;color:var(--ink);margin-bottom:1px}
.service p,.product p{
  font-family:"Arimo",sans-serif;font-size:9.6px;line-height:11.6px;color:var(--ink-soft);text-align:justify;
}
.column-divider{position:absolute;left:334px;top:335px;width:1px;height:285px;background:#e3e6e9}
.products{
  position:absolute;left:358px;top:327px;width:263px;height:311px;border:2px solid var(--note-red);
  padding:6px 10px 0 11px;
}
.product{display:flex;gap:15px;height:162px}
.product__cover{width:112px;flex:none;border:1px solid #dcdcdc}
.product__cover--science{height:143px;background:linear-gradient(180deg,#fff 0%,#fbe97a 45%,#f0cf18 100%)}
.product__cover--stats{height:123px;background:linear-gradient(180deg,#fff 0%,#f3b6d6 25%,#fff 55%,#eef0f2 100%)}
.product h3{font-family:"Arimo",sans-serif;font-weight:400;font-size:11px;color:var(--ink);margin-bottom:2px}
.product p+p{margin-top:11px}
.more-button{
  position:absolute;top:648px;width:96px;height:25px;
  background:linear-gradient(180deg,#18a64e,var(--green-dark));
  clip-path:polygon(12px 0,100% 0,100% 100%,0 100%);
  color:#fff;font-size:10.5px;font-weight:600;line-height:25px;text-align:center;padding-left:8px;
}
.more-button--services{left:198px}.more-button--products{left:512px}
.footer{position:absolute;left:0;top:858px;width:1200px;text-align:center;font-size:8px;color:#fff;letter-spacing:.4px}
.notes{position:absolute;left:0;top:0;width:1200px;height:900px;pointer-events:none}
.note{position:absolute;font-size:7.8px;font-weight:600;color:var(--note-ink);text-transform:uppercase;line-height:11px}
</style>
</head>
<body>
<div class="printer-body"></div>
<div class="printer-window"></div>
<div class="rail rail--left"></div>
<div class="rail rail--right"></div>

<div class="brand"><span class="brand__mark"></span>GLÓPRENT</div>

<div class="tool-button tool-button--cart" title="Karfa"></div>
<div class="tool-button tool-button--design" title="Hönnun"></div>
<div class="slider"></div>
<div class="tool-label">GLÓPRENT</div>

<nav class="main-nav">
  <a class="is-active" href="#">HEIM</a>
  <a href="#">ÞJÓNUSTA</a>
  <a href="#">SKIL Á VERKUM</a>
  <a href="#">GLÓPRENT</a>
  <a href="#">HVAR ERUM VIÐ</a>
</nav>

<main class="sheet">
  <div class="hero" role="img" aria-label="Banner: printer with swirling colourful paper and a person with a laptop">
    <div class="hero__title">GLÓPRENT</div>
  </div>

  <div class="section-ribbon">ÞJÓNUSTA</div>
  <h2 class="section-title">VÖRUR</h2>

  <section class="services">
    <article class="service">
      <svg class="service__icon" viewBox="0 0 60 60" aria-hidden="true">
        <rect x="18" y="2" width="24" height="18" fill="var(--yellow)"/>
        <rect x="6" y="20" width="48" height="22" rx="3" fill="var(--yellow)"/>
        <rect x="16" y="36" width="28" height="16" fill="#ffd94a"/>
      </svg>
      <div>
        <h3>LJÓSRITUN</h3>
        <p>Við tökum að okkar að ljósrita í lit eða svart hvítu, við fjölritum námshefti, námsgögn, greinasöfn, MA ritgerðir, BA ritgerðir, handrit, spurningalista og fleira og bindum inn á þann hátt sem hentar. Við gormum, kjölllímum og heftum, brjótum og skerum; allt eftir þínu höfði. Við skönnum inn í tölvu á hvaða formi sem hentar þér.</p>
      </div>
    </article>
    <article class="service">
      <svg class="service__icon" viewBox="0 0 60 60" aria-hidden="true">
        <path d="M22 2h20l10 10v32H22z" fill="var(--green-dark)"/>
        <path d="M8 16h20l10 10v32H8z" fill="var(--green)" stroke="#fff" stroke-width="2"/>
      </svg>
      <div>
        <h3>PRENTUN</h3>
        <p>Við sjáum um alla almenna prentun, til dæmis prentun við: bæklinga, dreifibréf, tímarit, nafnspjöld, ársskýrslur, boðskort, ráðstefnugögn, markpóst, plaköt og skilum því eins og hentar þér best. Við getum prentað á fjölmargar tegundir pappírs, þykkan, þunnan, gljáandi eða mattan.</p>
      </div>
    </article>
    <article class="service">
      <svg class="service__icon" viewBox="0 0 60 60" aria-hidden="true">
        <path d="M4 12c8-4 18-4 26 2v38c-8-6-18-6-26-2z" fill="var(--red)"/>
        <path d="M56 12c-8-4-18-4-26 2v38c8-6 18-6 26-2z" fill="var(--red)"/>
        <path d="M36 10v16l4-4 4 4V8z" fill="#fff"/>
      </svg>
      <div>
        <h3>BÓKAÚTGÁFA</h3>
        <p>Við gefum út bækur, ekkert upplag er of lítið eða stórt. Við höfum prentað námsbækur, kennslubækur, barnabækur, spennubækur, eða allar tegundir bóka. Við skilum bókum sem kilju, harðspjaldabók, í möppu, leðurbundið eða hvað sem hentar. Við getum skannað inn gamlar bækur og endurútgefið.</p>
      </div>
    </article>
  </section>

  <div class="column-divider"></div>

  <section class="products">
    <article class="product">
      <div class="product__cover product__cover--science" role="img" aria-label="Yellow textbook cover with triangle pattern"></div>
      <div>
        <h3>Námshefti</h3>
        <p>Við framleiðum námshefti fyrir fjölmarga skóla eftir óskum kennara.</p>
        <p>Hægt er að prenta einungis það magn sem selt er og tryggja þannig að bækur séu ekki með úreldum upplýsingum</p>
      </div>
    </article>
    <article class="product">
      <div class="product__cover product__cover--stats" role="img" aria-label="White textbook cover with pink title band"></div>
      <div>
        <h3>Kennslubækur</h3>
        <p>Við prentum kennslubækur fyrir marga skóla, bæði gormainnbundnar og kiljuinnbundnar.</p>
        <p>Hægt er að prenta einungis það magn sem selt er og spara sér þannig töluverðan kostnað við lagerhald.</p>
      </div>
    </article>
  </section>

  <a class="more-button more-button--services">LESA MEIRA</a>
  <a class="more-button more-button--products">LESA MEIRA</a>
</main>

<svg class="notes" viewBox="0 0 1200 900" aria-hidden="true">
  <g fill="none" stroke="var(--note-red)">
    <circle cx="874" cy="21" r="20" stroke-width="2.5"/>
    <circle cx="941" cy="21" r="20" stroke-width="2.5"/>
  </g>
  <g stroke="#0b2f66" stroke-width="1">
    <line x1="952" y1="38" x2="1040" y2="108"/>
    <line x1="885" y1="40" x2="992" y2="138"/>
    <line x1="882" y1="270" x2="962" y2="340"/>
    <line x1="912" y1="600" x2="962" y2="645"/>
  </g>
</svg>
<div class="note" style="left:1040px;top:109px">Demo/Design tool</div>
<div class="note" style="left:996px;top:139px">Shopping cart</div>
<div class="note" style="left:964px;top:342px">Animated banner (few images changing)</div>
<div class="note" style="left:964px;top:643px">A running table showing as many<br>products as you want</div>

<footer class="footer">COPYRIGHT © 2013 GLÓPRENT. ALL RIGHTS RESERVED.</footer>
</body>
</html>
```